One business card required with 2 company logos and 2 people's details

One business card required.
No preference on design - One side could show the 2 different business logos for the companies we own. The reverse could have the details shown below.
Another option could be one business one side and one business on the reverse. Happy to receive designs.

Carol Denbigh
07700 318 274
Rachel Tolland
07700 582 036

website: truelymarvellous.example
email: info@truelymarvellous.example

website: ironwillowevents.example
email: info:ironwillowevents.example

May be nice to have icons instead of the words email/website?

I have included different versions of the logos to help with your design.

Contact Information for Business Card

see project overview

Requirements
Must have
• both company logos, both contact names and contact details

```html
<!DOCTYPE html>
<html lang="en">
<head>
<meta charset="utf-8">
<title>Business Card – Iron Willow Events &amp; Truely Marvellous</title>
<link href="https://fonts.googleapis.com/css2?family=Open+Sans:wght@400;600;700&display=swap" rel="stylesheet">
<style>
  :root {
    --backdrop: #d9d9d7;
    --card-white: #fbfbfa;
    --card-edge: #1f5fd0;
    --ink-grey: #4a4d52;
    --rule-grey: #8a8d92;
    --name-deep: #1d3fa8;
    --name-bright: #1aa3d6;
    --night-dark: #0c141c;
    --night-teal: #123847;
    --logo-blue: #3d7fe0;
    --logo-ice: #e9f3f8;
    --ring-teal: #4fb7d6;
  }
  * { box-sizing: border-box; margin: 0; padding: 0; }
  html, body { width: 1200px; height: 801px; overflow: hidden; }
  body {
    background: var(--backdrop);
    font-family: "Open Sans", Arial, sans-serif;
    position: relative;
  }
  .card {
    position: absolute;
    top: 232px;
    width: 520px;
    height: 336px;
    border-bottom: 4px solid var(--card-edge);
    box-shadow: 0 10px 28px rgba(0,0,0,0.18);
  }
  .card--contacts { left: 50px; background: var(--card-white); }
  .card--logos {
    left: 630px;
    background:
      radial-gradient(circle at 70% 45%, var(--night-teal) 0%, rgba(18,56,71,0) 55%),
      var(--night-dark);
  }

  /* Contacts side */
  .contacts {
    position: absolute;
    inset: 0;
    display: flex;
    align-items: center;
    justify-content: center;
  }
  .person { width: 230px; color: var(--ink-grey); font-size: 12.5px; line-height: 1.55; }
  .person--left { text-align: right; padding-right: 14px; }
  .person--right { text-align: left; padding-left: 14px; }
  .divider { width: 1px; height: 72px; background: var(--rule-grey); align-self: flex-start; margin-top: 128px; }
  .person__name {
    font-weight: 700;
    font-size: 17px;
    letter-spacing: 0.3px;
    text-transform: uppercase;
    margin-bottom: 2px;
  }
  .person__first { color: var(--name-deep); }
  .person__last { color: var(--name-bright); }
  .person__phone { margin-bottom: 14px; }
  .contact-line { display: flex; align-items: center; gap: 6px; white-space: nowrap; }
  .person--left .contact-line { justify-content: flex-end; }
  .icon { width: 11px; height: 11px; flex: none; }

  /* Logos side */
  .brand {
    position: absolute;
    display: flex;
    align-items: center;
    gap: 10px;
    font-weight: 600;
  }
  .brand--willow { left: 40px; top: 150px; color: var(--logo-blue); font-size: 20px; }
  .brand--marvel { left: 275px; top: 150px; color: var(--logo-ice); font-size: 20px; }
  .brand__dot { width: 14px; height: 14px; border-radius: 50%; flex: none; }
  .brand--willow .brand__dot { background: var(--logo-blue); }
  .brand--marvel .brand__dot { background: var(--ring-teal); }
</style>
</head>
<body>

<section class="card card--contacts" aria-label="Contact side">
  <div class="contacts">
    <div class="person person--left">
      <p class="person__name"><span class="person__first">Rachel</span> <span class="person__last">Tolland</span></p>
      <p class="person__phone">07700 582 036</p>
      <p class="contact-line">info:ironwillowevents.example
        <svg class="icon" viewBox="0 0 12 12"><rect x="0.5" y="2" width="11" height="8" rx="1" fill="var(--card-edge)"/><path d="M1 2.5 6 6.5 11 2.5" stroke="#fff" fill="none" stroke-width="1"/></svg></p>
      <p class="contact-line">ironwillowevents.example
        <svg class="icon" viewBox="0 0 12 12"><circle cx="6" cy="6" r="5.5" fill="var(--card-edge)"/><path d="M0.5 6h11M6 0.5c-2.5 3-2.5 8 0 11M6 0.5c2.5 3 2.5 8 0 11" stroke="#fff" fill="none" stroke-width="0.8"/></svg></p>
    </div>
    <div class="divider"></div>
    <div class="person person--right">
      <p class="person__name"><span class="person__first">Carol</span> <span class="person__last">Denbigh</span></p>
      <p class="person__phone">07700 318 274</p>
      <p class="contact-line">
        <svg class="icon" viewBox="0 0 12 12"><rect x="0.5" y="2" width="11" height="8" rx="1" fill="var(--card-edge)"/><path d="M1 2.5 6 6.5 11 2.5" stroke="#fff" fill="none" stroke-width="1"/></svg>info@truelymarvellous.example</p>
      <p class="contact-line">
        <svg class="icon" viewBox="0 0 12 12"><circle cx="6" cy="6" r="5.5" fill="var(--card-edge)"/><path d="M0.5 6h11M6 0.5c-2.5 3-2.5 8 0 11M6 0.5c2.5 3 2.5 8 0 11" stroke="#fff" fill="none" stroke-width="0.8"/></svg>truelymarvellous.example</p>
    </div>
  </div>
</section>

<section class="card card--logos" aria-label="Logo side">
  <div class="brand brand--willow"><span class="brand__dot"></span>Iron Willow Events</div>
  <div class="brand brand--marvel"><span class="brand__dot"></span>Truely Marvellous</div>
</section>

</body>
</html>
```